Stroke Process

I need to create an infographic design that can help me explain the process of a new project that I am working on. The project is a step by step illustration on what needs to be done in order to get a stroke patient that proper wheelchair.

The graphics should walk a client through the process starting with #1 in the inpatient process and the explanation of the steps through the last step in the outpatient process. I uploaded two documents but the document with the explanation is the document to build the illustration on. This is a healthcare piece so the graphics should represent healthcare

```html
<!DOCTYPE html>
<html lang="en">
<head>
<meta charset="utf-8">
<title>Stroke Patient Process</title>
<link href="https://fonts.googleapis.com/css2?family=Oswald:wght@500;600;700&family=Raleway:wght@500;600;700;800&display=swap" rel="stylesheet">
<style>
:root{
  --navy:#1e3d8f;
  --band:#203f93;
  --panel:#4a8ee0;
  --panel-dark:#4287db;
  --chip:#8fd3f5;
  --cyan:#c8f1ff;
  --white:#ffffff;
  --ink:#1b2a55;
}
*{margin:0;padding:0;box-sizing:border-box}
html,body{width:927px;height:1200px;overflow:hidden;background:var(--white)}
.canvas{position:relative;width:927px;height:1200px;overflow:hidden;background:var(--white);font-family:"Raleway",sans-serif;color:var(--white)}
.abs{position:absolute}
.header{left:0;top:0;width:927px;height:72px;background:var(--band)}
.title{left:0;top:4px;width:927px;text-align:center;font-family:"Oswald",sans-serif;font-weight:700;font-size:40px;letter-spacing:1px;color:var(--white);line-height:56px}
.title-rule{left:270px;top:62px;width:387px;height:3px;background:var(--white)}
.reason-title{left:23px;top:82px;font-family:"Oswald",sans-serif;font-weight:600;font-size:19px;color:var(--navy);line-height:26px;letter-spacing:.2px}
.reason-text{left:23px;top:108px;width:885px;font-size:14px;font-weight:500;line-height:18.8px;color:var(--ink)}
.columns-band{left:0;top:224px;width:927px;height:32px;background:var(--band)}
.col-label{top:224px;font-family:"Oswald",sans-serif;font-weight:500;font-size:17px;line-height:32px;text-align:center;letter-spacing:.4px}
.panel{top:256px;height:930px;background:var(--panel)}
.panel-left{left:0;width:462px}
.panel-right{left:462px;width:465px;background:var(--panel-dark)}
.divider{left:461px;top:262px;height:920px;border-left:2px dashed rgba(255,255,255,.85)}
.bottom-stripe{left:0;top:1186px;width:927px;height:14px;background:var(--band)}
.num{width:26px;height:26px;background:var(--chip);color:var(--white);font-family:"Oswald",sans-serif;font-weight:600;font-size:19px;text-align:center;line-height:26px}
.heading{font-weight:700;font-size:16px;line-height:21px;color:var(--cyan)}
.text{font-size:14.5px;font-weight:500;line-height:19.6px}
.list{list-style:none}
.list li{position:relative;padding-left:24px;font-size:14.5px;font-weight:500;line-height:19.6px}
.list li::before{content:"•";position:absolute;left:6px;top:0}
.callout{font-weight:700;color:var(--cyan);font-size:14.5px;line-height:19.6px}
.code{font-size:14.5px;font-weight:500;line-height:20px}
.send{font-size:14.5px;font-weight:600;line-height:20px}
.contact{font-size:13.5px;font-weight:500;line-height:18.4px}
.art{border-radius:6px}
.art-discharge{left:288px;top:318px;width:114px;height:122px;background:linear-gradient(160deg,#bfe3fb,#5d9fe6)}
.art-hospital{left:273px;top:523px;width:129px;height:101px;background:linear-gradient(180deg,#d8f0ff,#2f77c9)}
.art-avatar{left:348px;top:677px;width:61px;height:61px;border-radius:50%;background:var(--white)}
.art-room{left:727px;top:985px;width:182px;height:182px;border-radius:0;background:linear-gradient(180deg,#eaf4fa,#f3a85a)}
.out-intro .num{float:left;margin:0 7px 0 -7px;height:26px}
.happy{left:490px;top:1130px;font-weight:800;font-size:23px;color:var(--navy);line-height:30px}
.happy span{color:var(--white);margin-right:14px}
</style>
</head>
<body>
<div class="canvas">
  <div class="abs header"></div>
  <h1 class="abs title">STROKE PATIENT PROCESS</h1>
  <div class="abs title-rule"></div>

  <h2 class="abs reason-title">REASON FOR FOLLOWING PROCESS RECOMMENDATIONS:</h2>
  <p class="abs reason-text">Insurance stroke clients are often discharged before it can be ascertained which mobility equipment will best suit their mobility needs and allow them to perform/participate in their Activities of Daily Living. Yet they require a wheelchair to be discharged. Therefore a rental chair is currently requested which can cause many issues when trying to get Medicare to approve appropriate mobility equipment when specific client issues can be ascertained and documented.</p>

  <div class="abs columns-band"></div>
  <div class="abs col-label" style="left:0;width:462px">IN PATIENT PROCESS</div>
  <div class="abs col-label" style="left:462px;width:465px">OUT PATIENT PROCESS</div>
  <div class="abs panel panel-left"></div>
  <div class="abs panel panel-right"></div>
  <div class="abs divider"></div>

  <!-- In patient: step 1 -->
  <div class="abs num" style="left:23px;top:287px">1</div>
  <h3 class="abs heading" style="left:61px;top:290px">Prior to Patient Discharge</h3>
  <ul class="abs list" style="left:33px;top:331px;width:210px">
    <li>Mobility Partners Group to bring “loaner” chair</li>
    <li>No charge invoice given to patient</li>
    <li>Transport Chair</li>
    <li>Standard Chair</li>
  </ul>
  <div class="abs art art-discharge" role="img" aria-label="Illustration of a nurse standing behind a patient in a wheelchair"></div>

  <!-- step 2 -->
  <div class="abs num" style="left:23px;top:484px">2</div>
  <h3 class="abs heading" style="left:61px;top:487px;width:395px">Patient admitted into Facility With CVA left or right side</h3>
  <ul class="abs list" style="left:33px;top:553px;width:230px">
    <li>46,000 diagnosis in Southern California</li>
    <li>25% Hemiplegia or Hemiparesis</li>
  </ul>
  <div class="abs art art-hospital" role="img" aria-label="Illustration of a hospital building with an ambulance"></div>

  <!-- step 3 -->
  <div class="abs num" style="left:23px;top:660px">3</div>
  <h3 class="abs heading" style="left:61px;top:663px">Diagnosed with Hemiplegia<br>or Hemiparesis</h3>
  <span class="abs code" style="left:29px;top:724px">I69.90</span>
  <span class="abs code" style="left:106px;top:724px">Late effects of CVA</span>
  <span class="abs code" style="left:48px;top:744px">(Cerebrovascular Accident)</span>
  <span class="abs code" style="left:29px;top:764px">I681.90</span>
  <span class="abs code" style="left:106px;top:764px">Hemiplegia</span>
  <span class="abs code" style="left:29px;top:785px">I69.354</span>
  <span class="abs code" style="left:106px;top:785px">Hemiparesis</span>
  <span class="abs send" style="left:280px;top:744px">Send:</span>
  <div class="abs art art-avatar" role="img" aria-label="Round avatar of a nurse"></div>
  <p class="abs contact" style="left:336px;top:746px">Mobility<br>Partners Group<br>800.555.0147<br>Face sheet</p>

  <!-- step 4 -->
  <div class="abs num" style="left:23px;top:843px">4</div>
  <h3 class="abs heading" style="left:61px;top:846px">Evaluation</h3>
  <p class="abs text" style="left:23px;top:873px;width:400px;line-height:20.5px">Evaluation with Physical Therapist for functional level. Mobility equipment decision and optimal seating will be based on all the findings from evaluation. Notes from evaluation submitted to therapist which include</p>
  <ul class="abs list" style="left:23px;top:955px;width:400px">
    <li>Seating mobility issues to be addressed</li>
    <li>Equipment considered and not chosen with rationale</li>
    <li>Equipment recommended and why client requires each item</li>
    <li>Expected Outcome Reasons for custom power wheelchair vs. transport or standard wheelchair add back benefits of Custom Wheelchair and Manual chair</li>
  </ul>

  <!-- Out patient: step 1 -->
  <div class="abs out-intro text" style="left:495px;top:283px;width:412px">
    <div class="num">1</div>
    <p style="padding-left:0">We will measure doorways and look for ingress and egress issues with the residence. Looking for special obstacles such as split level floors, high thresh holds, furniture lay out or uneven exterior pathways. Access issues can cause possible issues with independent mobility and ADL’s</p>
  </div>
  <p class="abs callout" style="left:495px;top:414px;width:410px">Important part of the process to determine how patient will use equipment in their own environment</p>
  <ul class="abs list" style="left:500px;top:474px;width:405px">
    <li>Are there obstacles that need to be removed so patient can operate equipment for ADL’s</li>
    <li>Is a manual chair or power chair better for patient in their home environment</li>
    <li>Measurements for door ways and thresholds</li>
    <li>Community based activities</li>
  </ul>

  <!-- step 2 -->
  <div class="abs num" style="left:488px;top:624px">2</div>
  <h3 class="abs heading" style="left:527px;top:624px">Completion of final documentation<br>and compliance review</h3>
  <ul class="abs list" style="left:500px;top:672px;width:410px">
    <li>Therapist reviews all notes and combines with PT evaluation to create Letter of Medical Justification</li>
    <li>Letter is signed and submitted to patients MD for patient face to face visit and modifications or con</li>
    <li>All paperwork is submitted for payor approval</li>
    <li>Equipment is ordered</li>
    <li>Equipment is assembled to patient recommended configuration</li>
  </ul>

  <!-- step 3 -->
  <div class="abs num" style="left:488px;top:872px">3</div>
  <h3 class="abs heading" style="left:527px;top:875px">Delivery of Custom Equipment</h3>
  <p class="abs text" style="left:492px;top:913px">Payor final approval</p>
  <p class="abs callout" style="left:492px;top:948px;width:330px">Equipment is delivered, fit and operational training</p>
  <ul class="abs list" style="left:500px;top:999px;width:200px">
    <li>Review equipment with patient</li>
    <li>Verify that equipment is configured correctly and adjustments made if necessary</li>
  </ul>
  <p class="abs happy"><span>•</span>Happy Patient</p>
  <div class="abs art art-room" role="img" aria-label="Illustration of a nurse with a patient in a wheelchair in a living room"></div>

  <div class="abs bottom-stripe"></div>
</div>
</body>
</html>
```